The Velvet Heron Espresso Nook Coffee Card

would like a coffee card designed for our café. Most cards are so boring and I need to stand out from the crowd (The Velvet Heron ). I require our logo on one side or the business name also a place for people to write their name and mobile number (collecting data base) and on the back the following
customer gets a stamp for the 1st three coffees purchased, on the 3rd one they get a free upsize. another 2 stamps and on the 3rd one (6) gets a free coffee, another 2 stamps and the customer gets another upsize (9th coffee purchased) and on the 10th card they recivie a voucher for a free pizza.
small print | one free pizza for dinner dining (not available for takeaways and must book), Cant be used with any other offers, opts in to hear from the herd if there is a deal on. cant trade for cash or gift

```html
<!DOCTYPE html>
<html lang="en">
<head>
<meta charset="utf-8">
<title>The Velvet Heron Espresso Nook – Coffee Card</title>
<link rel="stylesheet" href="https://fonts.googleapis.com/css2?family=Oswald:wght@500;700&family=Lato:wght@400&display=swap">
<style>
  :root {
    --backdrop: #3a322e;
    --card-light: #f4f4f2;
    --card-dark: #121212;
    --ink: #151515;
    --ink-soft: #6a6a6a;
    --rule-light: #9a9a9a;
    --rule-dark: #4a4a4a;
    --paper-text: #e6e6e6;
  }
  * { box-sizing: border-box; margin: 0; padding: 0; }
  html, body { width: 1200px; height: 844px; overflow: hidden; }
  body {
    background: var(--backdrop);
    font-family: "Lato", sans-serif;
    position: relative;
  }
  .card {
    position: absolute;
    top: 262px;
    width: 520px;
    height: 300px;
    box-shadow: 0 14px 30px rgba(0,0,0,.45);
  }
  .card--front { left: 50px; background: var(--card-light); color: var(--ink); }
  .card--back  { left: 630px; background: var(--card-dark); color: var(--paper-text); }

  /* Front: brand panel */
  .brand {
    position: absolute;
    left: 34px; top: 0; width: 224px; height: 100%;
    display: flex; flex-direction: column; justify-content: flex-end;
    padding-bottom: 62px;
  }
  .brand__mark {
    width: 22px; height: 22px;
    background: var(--ink);
    margin-bottom: 12px;
  }
  .brand__name {
    font-family: "Oswald", sans-serif;
    font-weight: 700;
    font-size: 31px;
    line-height: 1;
    text-transform: uppercase;
    letter-spacing: .5px;
    color: var(--ink);
    padding-bottom: 8px;
    border-bottom: 1px solid var(--rule-light);
  }
  .brand__tagline {
    font-size: 11px;
    letter-spacing: 2px;
    text-transform: uppercase;
    color: var(--ink-soft);
    text-align: center;
    margin-top: 6px;
  }
  .divider {
    position: absolute;
    left: 282px; top: 38px; bottom: 38px;
    border-left: 1px solid var(--rule-light);
  }

  /* Front: customer details */
  .details {
    position: absolute;
    left: 282px; right: 0; top: 90px;
  }
  .details__field {
    height: 62px;
    display: flex; align-items: center;
    padding-left: 22px;
    border-bottom: 1px solid var(--rule-light);
    font-family: "Oswald", sans-serif;
    font-weight: 500;
    font-size: 21px;
    text-transform: uppercase;
    color: var(--ink);
  }

  /* Back: rules and small print */
  .terms {
    position: absolute;
    left: 34px; right: 34px; top: 38px;
  }
  .terms__rules {
    font-size: 12.5px;
    line-height: 1.5;
    padding: 14px 0 16px;
    border-top: 1px solid var(--rule-dark);
    border-bottom: 1px solid var(--rule-dark);
  }
  .terms__fine {
    font-size: 10.5px;
    line-height: 1.5;
    padding-top: 16px;
    color: #cfcfcf;
  }
</style>
</head>
<body>
  <section class="card card--front" aria-label="Coffee card front">
    <div class="brand">
      <span class="brand__mark" aria-hidden="true"></span>
      <h1 class="brand__name">The Velvet Heron</h1>
      <p class="brand__tagline">Espresso Nook</p>
    </div>
    <div class="divider" aria-hidden="true"></div>
    <div class="details">
      <div class="details__field">Name</div>
      <div class="details__field">Mobile</div>
    </div>
  </section>

  <section class="card card--back" aria-label="Coffee card back">
    <div class="terms">
      <p class="terms__rules">Customer gets a stamp for the 1st three coffees purchased, on the 3rd one they get a free upsize. another 2 stamps and on the 3rd one (6) gets a free coffee, another 2 stamps and the customer gets another upsize (9th coffee purchased) and on the 10th card they recivie a voucher for a free pizza.</p>
      <p class="terms__fine">One free pizza for dinner dining (not available for takeaways and must book), Cant be used with any other offers, opts in to hear from the herd if there is a deal on.<br>Cant trade for cash or gift</p>
    </div>
  </section>
</body>
</html>
```